Pixel Harbor Business Card

I have attached several examples of business cards that I have seen online that I liked. We will be incorporating Spot UV coating and raised ink on the cards. Optionally we may use embossing with color. The business card will be used for 3d printing services. We are hoping to see some different color options of cards (i.e. black card, white card, etc.). We look forward to your ideas.

• Dorian Kest
Founder and CEO
+1.555.000.0000 cell
+1.000.000.0001 office
+1.000.000.0001 fax
Dorian.Kest@3dVorlanix.example
www.3dVorlanix.example
• I would be nice to see some 3d background designs to add some depth to the designs of the cards since it is a 3d design company. There are examples of this in the files I have attached.

```html
<!DOCTYPE html>
<html lang="en">
<head>
<meta charset="utf-8">
<title>Vorlanix Business Card</title>
<link href="https://fonts.googleapis.com/css2?family=Open+Sans:wght@400;700&display=swap" rel="stylesheet">
<style>
  :root {
    --backdrop: #ececec;
    --card-light: #e6e6e4;
    --card-mid: #d9d9d7;
    --panel: rgba(150, 150, 150, 0.22);
    --ink-dark: #2f2f2f;
    --ink-body: #3a3a3a;
    --accent-orange: #d9560f;
    --mark-dark: #1f1f1f;
  }
  * { margin: 0; padding: 0; box-sizing: border-box; }
  html, body { width: 1200px; height: 1152px; overflow: hidden; }
  body {
    background: var(--backdrop);
    font-family: "Open Sans", sans-serif;
    position: relative;
  }
  .card {
    position: absolute;
    left: 150px;
    width: 900px;
    height: 514px;
    overflow: hidden;
    border-radius: 4px;
    background:
      radial-gradient(ellipse at 30% 20%, rgba(255,255,255,0.55), transparent 60%),
      radial-gradient(ellipse at 80% 90%, rgba(0,0,0,0.05), transparent 55%),
      linear-gradient(135deg, var(--card-light), var(--card-mid));
    box-shadow: 0 10px 30px rgba(0,0,0,0.18);
  }
  .card--front { top: 40px; }
  .card--back { top: 598px; }
  .panel {
    position: absolute;
    background: var(--panel);
    border-radius: 30px;
  }
  .card--front .panel--left { left: -30px; top: 110px; width: 280px; height: 360px; }
  .card--front .panel--right { left: 770px; top: 150px; width: 180px; height: 340px; }
  .card--back .panel--info { left: 20px; top: 150px; width: 630px; height: 300px; }
  .card--back .panel--right { left: 880px; top: 90px; width: 80px; height: 300px; }

  .brand {
    position: absolute;
    display: flex;
    flex-direction: column;
    align-items: center;
  }
  .brand__dot {
    border-radius: 50%;
    background: var(--mark-dark);
    flex: none;
  }
  .brand__name {
    font-weight: 400;
    color: var(--ink-dark);
    line-height: 1;
    white-space: nowrap;
  }
  .card--front .brand { left: 0; right: 0; top: 80px; gap: 36px; }
  .card--front .brand__dot { width: 200px; height: 200px; }
  .card--front .brand__name { font-size: 56px; letter-spacing: 0.35em; padding-left: 0.35em; }

  .card--back .brand { right: 36px; top: 100px; width: 240px; gap: 30px; }
  .card--back .brand__dot { width: 170px; height: 170px; }
  .card--back .brand__name { font-size: 30px; letter-spacing: 0.25em; padding-left: 0.25em; }

  .contact { position: absolute; left: 55px; top: 205px; }
  .contact__head { display: flex; align-items: baseline; gap: 14px; margin-bottom: 16px; white-space: nowrap; }
  .contact__name { font-weight: 700; font-size: 38px; color: var(--ink-dark); }
  .contact__role { font-weight: 700; font-size: 25px; color: var(--accent-orange); }
  .contact__list { list-style: none; padding-left: 45px; font-size: 21px; color: var(--ink-body); line-height: 1.75; white-space: nowrap; }
  .contact__label { color: var(--accent-orange); }
  .contact__url { color: var(--accent-orange); }
</style>
</head>
<body>
  <section class="card card--front" aria-label="Card front">
    <div class="panel panel--left"></div>
    <div class="panel panel--right"></div>
    <div class="brand">
      <span class="brand__dot"></span>
      <span class="brand__name">VORLANIX</span>
    </div>
  </section>

  <section class="card card--back" aria-label="Card back">
    <div class="panel panel--info"></div>
    <div class="panel panel--right"></div>
    <div class="contact">
      <div class="contact__head">
        <span class="contact__name">DORIAN KEST</span>
        <span class="contact__role">FOUNDER AND CEO</span>
      </div>
      <ul class="contact__list">
        <li><span class="contact__label">cel:</span> +1.555.000.0000</li>
        <li><span class="contact__label">tel:</span> +1.000.000.0001 <span class="contact__label">fax:</span> +1.000.000.0001</li>
        <li><span class="contact__label">mail:</span> Dorian.Kest@3dVorlanix.example</li>
        <li><span class="contact__label">url:</span> <span class="contact__url">www.3dVorlanix.example</span></li>
      </ul>
    </div>
    <div class="brand">
      <span class="brand__dot"></span>
      <span class="brand__name">VORLANIX</span>
    </div>
  </section>
</body>
</html>
```